Broschüre für Gebäudereinigungsservice
Zielgruppe
Wir sind ein Gebäudeservice Unterehmen. Wir sind spezialisiert auf: Reinigungen aller Art, Grünflächenpflege aller Art, Winterdienst und Handwerkerservice aller Art. Usere Zielgruppe: Hausverwaltungen, Genossenschaften und Privatpersonen.
Aufgabenstellung
Die Broschüre soll an diese Kunden per Mail als auch ausgedruckt versendet werden.
Kunden sollen mit dieser Broschüre davon überzeugt werden uns als Gebäudeservice-Unternehmen zu beauftragen.
Unser Firmenslogan lautet 'QUALITÄT DURCH LEISTUNG.'
Die Bilder im Anhang können übernommen werden. Müssen aber nicht, bin für besserer Vorschläge gerne zu haben.
Alle Formate sind erlaubt
Bei Fragen bitte kontaktieren.
Danke!

```html
<!DOCTYPE html>
<html lang="de">
<head>
<meta charset="utf-8">
<title>Dienstleistungsübersicht – Gebäudeservice</title>
<link href="https://fonts.googleapis.com/css2?family=Open+Sans:wght@400;700&display=swap" rel="stylesheet">
<style>
  :root {
    --paper: #fde4e3;
    --ink: #1c1c1c;
    --divider: #8c8585;
    --frame: #2a2a2a;
    --shadow: rgba(90, 60, 60, 0.35);
  }
  * { box-sizing: border-box; margin: 0; padding: 0; }
  html, body { width: 1200px; height: 849px; overflow: hidden; }
  body {
    background: var(--paper);
    font-family: "Open Sans", "DejaVu Sans", Arial, sans-serif;
    color: var(--ink);
  }
  .brochure { position: relative; width: 1200px; height: 849px; }

  .divider {
    position: absolute; left: 597px; top: 40px; width: 2px; height: 766px;
    background: var(--divider);
  }

  .page-title {
    position: absolute; left: 160px; width: 310px; top: 63px;
    text-align: center; font-size: 15.5px; font-weight: 700; text-decoration: underline;
  }
  .section-title {
    position: absolute; font-size: 15.5px; font-weight: 700; text-decoration: underline;
  }
  .service-list { position: absolute; list-style: none; white-space: nowrap; }
  .service-list li::before { content: "▹ "; font-size: 0.8em; }
  .align-right { text-align: right; }

  .cleaning-title { left: 40px; top: 88px; }
  .cleaning-list { left: 40px; top: 108px; font-size: 17px; line-height: 35px; }

  .garden-title { right: 612px; top: 473px; font-size: 17px; }
  .garden-list { right: 612px; top: 494px; font-size: 16.5px; line-height: 29.8px; }

  .winter-title { left: 606px; top: 39px; }
  .winter-list { left: 606px; top: 60px; font-size: 15px; line-height: 27.2px; }

  .clearance-title { right: 46px; top: 221px; }
  .clearance-list { right: 46px; top: 242px; font-size: 15px; line-height: 27.4px; }

  .craft-title { left: 606px; top: 448px; }
  .craft-list { left: 606px; top: 469px; font-size: 15px; line-height: 27.3px; }

  .photo {
    position: absolute; border-radius: 50%;
    border: 5px solid var(--frame);
    box-shadow: 0 2px 6px rgba(0,0,0,0.25);
  }
  .photo-cleaning { left: 352px; top: 121px; width: 206px; height: 206px;
    background: radial-gradient(circle at 45% 40%, #f4f4f2, #c9c6c0 70%, #8d7c6a); }
  .photo-garden { left: 75px; top: 492px; width: 206px; height: 206px;
    background: linear-gradient(180deg, #d8dccf 0%, #6aa63c 35%, #3f8a22 100%); }
  .photo-winter { left: 965px; top: 48px; width: 164px; height: 164px;
    background: linear-gradient(160deg, #b9b4ac 0%, #dfe3e6 55%, #f4f6f8 100%); }
  .photo-clearance { left: 650px; top: 226px; width: 176px; height: 176px;
    background: linear-gradient(180deg, #9a8c7a 0%, #8fa6b2 45%, #7d7b77 100%); }
  .photo-craft { left: 985px; top: 497px; width: 150px; height: 150px;
    background: radial-gradient(circle at 40% 45%, #c9a98e, #b4b8bb 60%, #dcdcd8); }

  .drop-shadow {
    position: absolute; border-radius: 50%;
    background: radial-gradient(ellipse at center, var(--shadow), rgba(90,60,60,0) 70%);
  }
  .shadow-cleaning { left: 365px; top: 350px; width: 180px; height: 50px; }
  .shadow-garden { left: 90px; top: 728px; width: 180px; height: 50px; }
  .shadow-craft { left: 1000px; top: 690px; width: 150px; height: 44px; }
</style>
</head>
<body>
<main class="brochure">
  <div class="divider"></div>

  <h1 class="page-title">Dienstleistungsübersicht</h1>

  <section>
    <h2 class="section-title cleaning-title">Hausreinigung:</h2>
    <ul class="service-list cleaning-list">
      <li>wöchentliche Stiegenhausreinigung</li>
      <li>Fensterreinigung</li>
      <li>Büroreinigung</li>
      <li>Wohnungsreinigung</li>
      <li>Reinigung Außenflächen</li>
      <li>Garagennassreinigung</li>
      <li>Fassadenreinigung</li>
      <li>Hochdruckreinigung</li>
      <li>Graffitientfernung</li>
      <li>diverse weitere Reinigungsarbeiten</li>
    </ul>
    <div class="drop-shadow shadow-cleaning"></div>
    <div class="photo photo-cleaning" role="img" aria-label="Reinigungskraft wischt einen hellen Flurboden mit Reinigungswagen"></div>
  </section>

  <section>
    <h2 class="section-title garden-title">Grünflächenpflege:</h2>
    <ul class="service-list garden-list align-right">
      <li>Rasenschnitt</li>
      <li>Rasenbewässerung</li>
      <li>Sträucherrückschnitt</li>
      <li>Baumkornenrückschitt</li>
      <li>Baumrodung</li>
      <li>Baumkronenabwurf</li>
      <li>Wurzelstockfräsung</li>
      <li>Efeubeseitigung</li>
      <li>Fertigrasenverlegung</li>
      <li>diverse weitere Grünflächenpflegearbeiten</li>
    </ul>
    <div class="drop-shadow shadow-garden"></div>
    <div class="photo photo-garden" role="img" aria-label="Rasenmäher auf frisch gemähtem grünem Rasen"></div>
  </section>

  <section>
    <h2 class="section-title winter-title">Winterdienst:</h2>
    <ul class="service-list winter-list">
      <li>Bereitschaftsdienst vom 01.11. bis 15.04.</li>
      <li>Schneeräumung</li>
      <li>Tauwetterkontrolle</li>
      <li>Splitt- und Salzstreuung</li>
      <li>Splittkehrung bei Trockenperioden</li>
      <li>händische als auch maschinelle Räumung</li>
    </ul>
    <div class="photo photo-winter" role="img" aria-label="Arbeiter in Warnweste räumt Schnee auf einem Gehweg am Geländer"></div>
  </section>

  <section>
    <h2 class="section-title clearance-title">Entrümpelung:</h2>
    <ul class="service-list clearance-list align-right">
      <li>Fachgerechte Abfallentsorgung</li>
      <li>Sperrmüllentsorgung</li>
      <li>Firmen- und Büroräumungen</li>
      <li>Wohnungsräumungen</li>
      <li>Verlassenschaftsräumungen</li>
      <li>Dachboden- und Kellerräumungen</li>
      <li>diverse weitere Räumungs- und Entrümpelungsarbeiten</li>
    </ul>
    <div class="photo photo-clearance" role="img" aria-label="Sperrmüll mit altem Fernseher und Matratzen am Straßenrand"></div>
  </section>

  <section>
    <h2 class="section-title craft-title">Handwerker-Service:</h2>
    <ul class="service-list craft-list">
      <li>Reparatur Türen und Fenster</li>
      <li>Kleinflächen verputzen und ausmalen</li>
      <li>Reparatur und Montage Geländer und Handläufe</li>
      <li>Montage Taubennetz und Taubenspitzen</li>
      <li>Reparatur und Montage Gullys</li>
      <li>Reparatur und Montage Türschließer</li>
      <li>Instandsetzung Kaminmauerwerk und Kaminköpfe</li>
      <li>Reparatur Holz-, Keramik- und Terazzoböden</li>
      <li>Montage Kantenschutzprofile</li>
      <li>Befestigung Boden- und Sockelfliesen</li>
      <li>Reparatur gebrochene Betonstufen</li>
      <li>diverse weitere Reparaturarbeiten</li>
    </ul>
    <div class="drop-shadow shadow-craft"></div>
    <div class="photo photo-craft" role="img" aria-label="Handwerker arbeitet mit Akkubohrer an einer Holzleiste"></div>
  </section>
</main>
</body>
</html>
```